Quorvella Website Redesign

We need a redesign of the company website.

We're a company, based in the UK, called Quorvella. We develop software for the Healthcare Industry, used by medical professionals throughout the UK on a daily basis.

We have a suite of tools that form the Quorvella Platform, and all are web-based.

We want to communicate that our software is not only innovative but is the best available, easy to use, and provides exceptional quality and RoI.

Additionally, we want our existing customers to be able to see what else we can offer them.

A site map is attached.
Updates

Hi Everyone,

As we approach the deadline for submissions, we’ve shortlisted threedesigns that we felt were the best of the submissions and have asked thedesigners to make some additional changes and produce some content pages so wecan see what’s beneath the Home page in the rest of the site.

Thank you all for your submissions – there was an awful lot ofdisagreement among everyone here over which designs we thought were best andsome of those that haven’t made it into the final three were very well liked.

Those in the final three have been messaged individually and have theirdesigns as the only non-eliminated ones showing. We would ask at this stagethat anyone not in the final three please do no further work or submitadditional designs as we are approaching the deadline and will not be able toprovide sufficient feedback to allow any changes in a short space of time.

Kind regards,
The Quorvella Team

Target Market(s)

Nurses and medical professionals in western-speaking countries, most notably in the UK.

Predominantly, we expect it will be senior medical staff that will be viewing (and using) our website - some will be existing customers and some will be new or potential customers.

Industry/Entity Type

Medical

Requirements
Must have
• Area to showcase and provide information about products.
• Company information - who we are and why you should choose us.
• News and events - blog, archive newsletters, publications, etc.
• Support section for existing customers - FAQ, Forum, Manuals.
• Contact page.
• We also feel that we'd like to have our telephone number and primary email address visible at all times, with an immediate ability for users to request a demonstration.
Nice to have
• A "My Quorvella" area would be nice at some point, though that's something for further down the line.

```html
<!DOCTYPE html>
<html lang="en">
<head>
<meta charset="utf-8">
<title>Quorvella Health – About Quorvella</title>
<link href="https://fonts.googleapis.com/css2?family=Open+Sans:wght@400;600;700&family=PT+Sans:wght@400;700&family=Source+Sans+3:wght@400;700&display=swap" rel="stylesheet">
<style>
:root{
  --page-bg:#05b4d6;
  --frame:#ffffff;
  --brand-blue:#1f8ee8;
  --heading-blue:#1aa0c8;
  --news-green:#2aa83a;
  --blog-orange:#e8560e;
  --orange:#f07a10;
  --ink:#444a50;
  --ink-soft:#6a7076;
  --nav-top:#e4e4e4;
  --nav-bottom:#b9b9b9;
  --subnav:#d8f0dc;
  --footer:#6f7882;
}
*{box-sizing:border-box;margin:0;padding:0}
html,body{width:933px;height:1200px;overflow:hidden}
body{background:var(--page-bg);font-family:"Open Sans",Arial,sans-serif;color:var(--ink);position:relative}
.frame{position:absolute;left:64px;top:58px;width:810px;height:1085px;background:var(--frame);border-radius:16px}
.abs{position:absolute}

/* header */
.header{left:70px;top:64px;width:800px;height:116px;border-radius:12px 12px 0 0;background:linear-gradient(180deg,#d6e5fb 0%,#eef4fd 60%,#dce9fb 100%)}
.brand{left:108px;top:82px;font-family:"PT Sans",sans-serif;font-weight:700;font-size:39px;line-height:46px;color:var(--brand-blue);letter-spacing:-.5px}
.brand-rule{left:108px;top:130px;width:288px;height:3px;background:#a9aeb4}
.tagline{left:108px;top:136px;font-family:"PT Sans",sans-serif;font-weight:700;font-size:17px;color:#8a8f95}
.contact-top{left:655px;top:94px;font-size:12px;line-height:17px;color:#4a4f55}
.contact-top b{color:var(--orange);font-weight:400}
.search{left:652px;top:140px}
.search-box{left:678px;top:142px;width:142px;height:15px;background:#fff;border:1px solid #c9d6e6;border-radius:3px;font-size:11px;color:#b7c2cf;padding-left:4px;line-height:13px}

/* nav */
.nav{left:68px;top:180px;width:804px;height:32px;display:flex;background:linear-gradient(180deg,var(--nav-top),var(--nav-bottom))}
.nav a{display:flex;align-items:center;justify-content:center;font-size:13px;color:#55595e;text-decoration:none;border-right:1px solid #a5a5a5;height:100%}
.nav a.active{background:linear-gradient(180deg,#f3f8fd,#d3e4f4);color:var(--brand-blue)}
.subnav{left:70px;top:212px;width:800px;height:21px;background:var(--subnav);display:flex;align-items:center;font-size:9.5px;color:#6c7a70}
.subnav span{white-space:nowrap}
.subnav .sep{width:5px;height:5px;background:#7fd0c9;margin:0 14px}
.subnav .current{color:var(--brand-blue)}

/* hero */
.hero{left:70px;top:235px;width:800px;height:192px;background:linear-gradient(180deg,#bfe6f4,#9fd7ec)}
.hero-corner{left:84px;top:252px}
.hero-title{left:108px;top:262px;z-index:2;font-family:"Source Sans 3",sans-serif;font-weight:400;font-size:28px;line-height:35px;color:#1c1f22;letter-spacing:-.4px;white-space:nowrap}
.hero-title strong{font-weight:700}
.hero-text{left:110px;top:337px;width:385px;font-size:10px;line-height:15px;color:#3d4a52}
.btn-orange{left:319px;top:388px;width:74px;height:21px;border-radius:4px;background:linear-gradient(180deg,#ffa13c,#ea5a08);color:#fff;font-size:11px;text-align:center;line-height:21px}
.hero-art{left:518px;top:240px;width:349px;height:200px;border-radius:6px;background:linear-gradient(135deg,#7f8fd6 0%,#b7e0f2 45%,#ffffff 75%,#cfe8f5 100%)}

/* left column */
.main-panel{left:78px;top:435px;width:518px;height:600px;border:1px solid #cbd7de;border-radius:10px;background:#f6faf9}
.card{position:absolute;left:93px;width:488px}
.card h2{font-family:"PT Sans",sans-serif;font-weight:400;font-size:21px;letter-spacing:-.2px}
.card p{font-size:9px;line-height:12px;color:var(--ink);text-indent:20px;margin-bottom:12px}
.card .more{position:absolute;left:0;bottom:0;width:100%;height:17px;font-size:10px;text-align:right;padding-right:22px;line-height:17px}
.about{top:447px;height:187px;background:linear-gradient(90deg,#e6f1ef,#f2f8f6)}
.about h2{color:var(--heading-blue);position:absolute;left:11px;top:8px}
.about .copy{position:absolute;left:11px;top:40px;width:215px}
.about .more{background:#c4ded8;color:#1a9ec8}
.about-art{left:335px;top:450px;width:230px;height:150px;background:linear-gradient(135deg,#dfe9ee,#9fb2bd 60%,#e6eef1)}
.news{top:643px;height:187px;background:linear-gradient(90deg,#e4ecdf,#f0f2ea)}
.news h2{color:var(--news-green);position:absolute;left:11px;top:8px}
.news .copy{position:absolute;left:11px;top:40px;width:466px}
.news .copy p{margin-bottom:10px}
.news .more{background:#cfe6dd;color:var(--news-green)}
.blog{top:840px;height:187px;background:linear-gradient(90deg,#e3ece6,#f3f2ea)}
.blog h2{color:var(--blog-orange);position:absolute;left:194px;top:8px}
.blog .copy{position:absolute;left:194px;top:40px;width:286px;text-align:justify}
.blog .more{background:#cfe6dd;color:var(--blog-orange)}
.feed-art{left:125px;top:855px;width:128px;height:125px;border-radius:16px;background:linear-gradient(160deg,#ff9a3c,#e8420a)}

/* sidebar */
.login{left:608px;top:433px;width:256px;height:232px;border-radius:12px;background:linear-gradient(180deg,#b3e5f5,#eef8fb);border:1px solid #cde7f1}
.login h3{position:absolute;left:32px;top:12px;font-family:"PT Sans",sans-serif;font-weight:400;font-size:28px;color:var(--brand-blue)}
.login .rule{position:absolute;left:32px;top:48px;width:168px;height:1px;background:#fff}
.login .user{position:absolute;left:22px;top:62px;font-family:"PT Sans",sans-serif;font-size:14px;color:#555}
.login .user b{font-weight:400;color:var(--orange)}
.field-label{position:absolute;left:21px;font-size:10px;color:#555}
.field{position:absolute;left:21px;width:216px;height:19px;background:#eef0f1;border:1px solid #d2d6d8;border-radius:3px;font-size:9px;color:#aaa;padding-left:8px;line-height:17px}
.check{position:absolute;left:24px;top:165px;width:12px;height:12px;border:1px solid #3aa9d0;background:#fff}
.remember{position:absolute;left:42px;top:166px;font-size:9.5px;color:#555}
.remember b{color:var(--orange);font-weight:400}
.btn-grey{position:absolute;border-radius:5px;background:linear-gradient(180deg,#f4f4f4,#c6c6c6);border:1px solid #aaa;color:#333;text-align:center;font-family:"PT Sans",sans-serif}
.login-links{position:absolute;left:26px;top:189px;font-size:9.5px;line-height:13px;color:#3a5870;text-decoration:underline}
.newsletter{left:608px;top:673px;width:255px;height:75px;border-radius:6px;background:linear-gradient(180deg,#6ddc63,#3bb637);border:1px solid #2ea03a}
.newsletter h3{position:absolute;left:18px;top:7px;font-family:"PT Sans",sans-serif;font-weight:400;font-size:20px;color:#254a26}
.newsletter .field{left:20px;top:41px;width:150px;height:21px;background:#f4f6f4;line-height:19px}
.demo{left:608px;top:754px;width:255px;height:41px;border-radius:5px;background:linear-gradient(180deg,#ff9d1e,#ed5a04);color:#fff;font-family:"PT Sans",sans-serif;font-weight:700;font-size:17px;text-align:center;line-height:41px;letter-spacing:.3px}
.archive{left:608px;top:802px;width:256px;height:232px;border-radius:12px;background:radial-gradient(ellipse at 50% 60%,#8ff27d 0%,#b6efa8 55%,#e9f6e6 100%);border:1px solid #d6ead1}
.archive h3{position:absolute;left:28px;top:12px;font-family:"PT Sans",sans-serif;font-weight:400;font-size:20px;color:#3b4a40}
.archive ul{position:absolute;left:46px;top:46px;list-style:none;font-family:"PT Sans",sans-serif;font-size:14.5px;line-height:20px}
.archive li{color:#2b3a30;text-decoration:underline}

/* footer */
.footer{left:70px;top:1043px;width:800px;height:95px;border-radius:0 0 12px 12px;background:linear-gradient(180deg,#737c86,#616a74);color:#fff;text-align:center;font-size:11.5px;line-height:15px;padding-top:10px}
.footer strong{font-weight:700}
.footer .gap{display:inline-block;width:14px}
</style>
</head>
<body>
<div class="frame"></div>

<header>
  <div class="abs header"></div>
  <div class="abs brand">Quorvella Health</div>
  <div class="abs brand-rule"></div>
  <div class="abs tagline">Bringing Technology to Healthcare</div>
  <div class="abs contact-top"><b>Call :</b> +44 (0) 208 555 0142<br><b>E-Mail :</b> support@quorvella.com</div>
  <svg class="abs search" width="26" height="26" viewBox="0 0 26 26" aria-hidden="true">
    <circle cx="10" cy="10" r="7" fill="#eaf3fb" stroke="#4a6a86" stroke-width="2"/>
    <line x1="15" y1="15" x2="23" y2="23" stroke="#3e5670" stroke-width="3.5" stroke-linecap="round"/>
  </svg>
  <div class="abs search-box">Search Quorvella</div>
</header>

<nav class="abs nav">
  <a style="width:87px">Home</a>
  <a style="width:143px">Products &amp; Services</a>
  <a class="active" style="width:124px">About Quorvella</a>
  <a style="width:134px">News and Events</a>
  <a style="width:86px">Support</a>
  <a style="width:100px">Contact us</a>
  <a style="width:130px;border-right:none">My Quorvella</a>
</nav>
<div class="abs subnav">
  <span style="margin-left:22px" class="current">About Quorvella</span><span class="sep"></span>
  <span>Leadership Team</span><span class="sep"></span>
  <span>Advisory Board</span><span class="sep"></span>
  <span>Partnerships</span><span class="sep"></span>
  <span>Experienced Clinical Staff</span><span class="sep"></span>
  <span>Medical Solutions Architects</span><span class="sep"></span>
  <span>Clients List</span>
</div>

<section>
  <div class="abs hero"></div>
  <div class="abs hero-art" role="img" aria-label="Team of medical professionals in white coats beside software discs"></div>
  <svg class="abs hero-corner" width="18" height="16" viewBox="0 0 18 16" aria-hidden="true"><path d="M0 0H18V16H12V6H0Z" fill="#fff"/></svg>
  <h1 class="abs hero-title">WE DEVELOPE SOFTWARES FOR THE<br><strong>HEALTHCARE</strong> INDUSTRY</h1>
  <p class="abs hero-text">We develop software for the Healthcare Industry, used by medical professionals throughout the UK on a daily basis. We have a suite of tools that form the Quorvella Platform, and all are web-based.</p>
  <div class="abs btn-orange">More Info</div>
</section>

<main>
  <div class="abs main-panel"></div>

  <article class="card about">
    <h2>ABOUT QUORVELLA</h2>
    <div class="copy">
      <p>In today's changing environment, healthcare organisations globally are faced with conflicting challenges; to reduce costs while offering improved healthcare services to patients that expect better and better services.</p>
      <p>Most health care organisations operate using either [rent technologies and systems that have been developed over a long period of time, ..........</p>
    </div>
    <div class="more">...... read more</div>
  </article>
  <div class="abs about-art" role="img" aria-label="Laptop with a doctor's hand holding a stethoscope out of the screen"></div>

  <article class="card news">
    <h2>NEWS AND UPDATES</h2>
    <div class="copy">
      <p>In today's changing environment, healthcare organisations globally are faced with conflicting challenges; to reduce costs while offering improved healthcare services to patients that expect better and better services.</p>
      <p>Most health care organisations operate using either manual paper based processed or a mix of different technologies and systems that have been developed over a long period of time, &nbsp;&nbsp;&nbsp; In today's changing environment, healthcare organisation<br>In today's changing environment, healthcare organisations globreduce costs while offering improved healthcare services to patients that expect better and better services.</p>
    </div>
    <div class="more">...... read more</div>
  </article>

  <article class="card blog">
    <h2>QUORVELLA NEWS BLOG</h2>
    <div class="copy">
      <p>In today's changing environment, healthcare organisations globally are faced with conflicting challenges; to reduce costs while offering improved healthcare services to patients that expect better and better services.</p>
      <p>Most health care organisations operate using either manual paper based processed or a mix of different technologies and systems that have been developed over avices to patients that expect better and better services.</p>
    </div>
    <div class="more">...... read more</div>
  </article>
  <div class="abs feed-art" role="img" aria-label="Large glossy orange news feed icon"></div>
</main>

<aside>
  <div class="abs login">
    <h3>Login</h3>
    <div class="rule"></div>
    <div class="user">You are logged in as <b>Daniel Harlow</b></div>
    <div class="field-label" style="top:89px">E-mail ID / Login ID</div>
    <div class="field" style="top:103px"></div>
    <div class="field-label" style="top:125px">Password</div>
    <div class="field" style="top:139px">••••••••••••••••</div>
    <div class="check"></div>
    <div class="remember">Remember <b>Me</b></div>
    <div class="btn-grey" style="left:161px;top:172px;width:76px;height:22px;font-size:14px;line-height:20px">Login</div>
    <div class="login-links">Forgot your passward?<br>Sign up here</div>
  </div>

  <div class="abs newsletter">
    <h3>Subscribe for Newsletter</h3>
    <div class="field">Enter your e-mail ID here</div>
    <div class="btn-grey" style="left:161px;top:40px;width:76px;height:23px;font-size:13px;line-height:21px">Subscribe</div>
  </div>

  <div class="abs demo">REQUEST A DEMO</div>

  <div class="abs archive">
    <h3>Archieved Newsletters</h3>
    <ul>
      <li>January 2009</li>
      <li>March 2009</li>
      <li>June 2009</li>
      <li>September 2009</li>
      <li>December 2009</li>
      <li>January 2010</li>
      <li>March 2010</li>
    </ul>
  </div>
</aside>

<footer class="abs footer">
  <strong>CONTACT INFORMATION</strong><br>
  Quorvella - # 48 Harrowfield Lane, London N4 2QT, United Kingdom<br>
  Tel.: +44 (0) 208 555 0142<span class="gap"></span>+44 (0) 208 555 0142<span class="gap"></span><strong>Fax:</strong> +44 (0) 208 555 0197<br>
  <strong>Republic Of Ireland</strong> - Tel.: +353 (0) 862 555 018<span class="gap"></span>+353 (0) 862 555 018<br>
  <strong>Greece and Cyprus</strong> - Tel.: +357 994 55021<span class="gap"></span>+357 994 55021
</footer>
</body>
</html>
```